Social Media Flyer Highlighting Real Estate Sale

Need a flyer made for a social media post highlighting the sale of a home. I am including a photo of the house, the same photo with what I would like the flyer to say that you design and a couple of inspiration images. I am with KVN Marlowe’s Estate Partners. It needs to have a luxury high end look.
For the flyer:
Use the house as a background for the flyer
Include the following text:
SOLD
Middleburg, VA
$1.3M
Dean Parrish, KVN Marlowe’s Estate Partners
(The Marlowe’s corporate colors are a navy blue and white with black font. See the examples)
Thank you!

Target Market(s)

Luxury Homeowners

Industry/Entity Type

Real Estate

Font styles to use
Other font styles liked:
• Serif font mercury is the primary typeface while Benton Sans is the secondary font

Colors
0054AA
0677BA
7BADD7
CADEEF
E8F1F8

Requirements
Must have
• A luxury high end look while keeping with the traditional Marlowe’s look at feel.

```html
<!DOCTYPE html>
<html lang="en">
<head>
<meta charset="utf-8">
<title>Sold – Middleburg, VA</title>
<link rel="stylesheet" href="https://fonts.googleapis.com/css2?family=Arimo:wght@400;700&family=Libre+Caslon+Text:wght@400;700&display=swap">
<style>
  :root {
    --page-bg: #e3ebfa;
    --label-ink: #444444;
    --navy-deep: #0f2f58;
    --navy-mid: #1a3d68;
    --sky: #5577a3;
    --foliage: #334f4c;
    --house: #5d6f82;
    --lawn: #2f5850;
    --white: #ffffff;
    --text-soft: #dde6f0;
    --price-ink: #c9d3d9;
    --brand-ink: #aebfcb;
    --shadow-ink: rgba(95, 110, 130, 0.85);
  }
  * { margin: 0; padding: 0; box-sizing: border-box; }
  html, body { width: 1200px; height: 1000px; overflow: hidden; }
  body {
    background: var(--page-bg);
    position: relative;
    font-family: "Arimo", Helvetica, Arial, sans-serif;
  }
  .status-label {
    position: absolute;
    left: 222px;
    top: 70px;
    font-size: 38px;
    font-weight: 700;
    letter-spacing: 0.5px;
    color: var(--label-ink);
  }
  .flyer {
    position: absolute;
    left: 225px;
    top: 148px;
    width: 750px;
    height: 589px;
    overflow: hidden;
    background: var(--navy-deep);
  }
  .house-photo {
    position: absolute;
    inset: 0;
    background:
      radial-gradient(ellipse 60% 28% at 60% 50%, rgba(110, 125, 140, 0.55), rgba(110, 125, 140, 0) 100%),
      radial-gradient(ellipse 45% 30% at 85% 8%, rgba(100, 130, 170, 0.6), rgba(100, 130, 170, 0) 100%),
      linear-gradient(180deg,
        var(--foliage) 0%,
        #3d5658 25%,
        var(--house) 48%,
        var(--lawn) 62%,
        #24486a 76%,
        var(--navy-mid) 84%,
        var(--navy-deep) 92%);
  }
  .sold-frame {
    position: absolute;
    left: 410px;
    top: 24px;
  }
  .sold-word {
    position: absolute;
    left: 412px;
    top: 40px;
    width: 296px;
    text-align: center;
    font-family: "Libre Caslon Text", Georgia, serif;
    font-size: 87px;
    letter-spacing: 3px;
    line-height: 1;
    color: var(--white);
    text-shadow: -9px 5px 0 var(--shadow-ink);
  }
  .sold-tagline {
    position: absolute;
    left: 412px;
    top: 126px;
    width: 296px;
    text-align: center;
    font-size: 24px;
    line-height: 1;
    color: var(--white);
  }
  .location {
    position: absolute;
    left: 62px;
    top: 426px;
    font-size: 31px;
    color: var(--text-soft);
  }
  .price {
    position: absolute;
    left: 58px;
    top: 475px;
    font-family: "Libre Caslon Text", Georgia, serif;
    font-size: 84px;
    letter-spacing: 4px;
    line-height: 1;
    color: var(--price-ink);
  }
  .agent-name {
    position: absolute;
    right: 44px;
    top: 448px;
    font-size: 29px;
    color: var(--text-soft);
  }
  .brokerage {
    position: absolute;
    right: 44px;
    top: 498px;
    font-size: 22px;
    line-height: 26px;
    text-align: right;
    color: var(--brand-ink);
  }
</style>
</head>
<body>
  <div class="status-label">REVISED</div>

  <section class="flyer">
    <div class="house-photo" role="img" aria-label="Photo of a two-storey cottage-style house with metal roofs, front porch and green lawn, trees behind, under a navy overlay"></div>

    <svg class="sold-frame" width="300" height="118" viewBox="0 0 300 118" aria-hidden="true">
      <polyline points="64,113 2,113 2,2 298,2 298,113 236,113" fill="none" stroke="#ffffff" stroke-width="2"/>
    </svg>
    <div class="sold-word">SOLD</div>
    <div class="sold-tagline">AND CLOSED</div>

    <div class="location">Middleburg, VA</div>
    <div class="price">$1.3M</div>

    <div class="agent-name">DEAN PARRISH</div>
    <div class="brokerage">KVN Marlowe’s<br>Estate Partners</div>
  </section>
</body>
</html>
```